Pitch Deck and business cards for Virtual Reality Startup

We need a redesign of our pitch deck to be funky, creative and interactive with animated graphics inline with our product (VR training)
Note: the design does not have to be orange that's just a template of the information we're sending you so we would like to see other colours also.

Target Market(s)

Investors

Industry/Entity Type

Media

Contact Information for Business Card

logo, Name, title, address, telephone, email, website

Font styles to use
Other font styles liked:
• funky but readable

Colors

Designer to choose colors to be used in the design.

Requirements
Must have
• Exciting non traditional design that fits a new, innovative, exciting and interactive technology
Nice to have
• .
Should not have
• traditional look and feel.

```html
<!DOCTYPE html>
<html lang="en">
<head>
<meta charset="utf-8">
<title>NOVAXR Pitch Deck</title>
<link href="https://fonts.googleapis.com/css2?family=Montserrat:wght@500;700;800;900&family=Quicksand:wght@500;600;700&display=swap" rel="stylesheet">
<style>
:root{
  --blue:#17a6e9;
  --purple:#6b2fa8;
  --ink:#3b1d6e;
  --text:#2b2b3a;
  --white:#ffffff;
  --dash:#8a7fc4;
  --grad:linear-gradient(90deg,var(--blue),var(--purple));
}
*{box-sizing:border-box;margin:0;padding:0}
html,body{width:1200px;height:628px;overflow:hidden;background:var(--white)}
body{position:relative;font-family:"Quicksand",sans-serif;color:var(--text)}
.sheet-title{position:absolute;top:14px;left:0;width:1200px;text-align:center;font-family:"Montserrat",sans-serif;font-weight:900;font-size:34px;letter-spacing:1.5px;color:var(--ink);line-height:1}
.sheet-sub{position:absolute;top:52px;left:0;width:1200px;text-align:center;font-family:"Montserrat",sans-serif;font-weight:500;font-size:26px;color:var(--ink);line-height:1}
.deck{position:absolute;top:105px;left:8px;display:grid;grid-template-columns:repeat(4,284px);grid-template-rows:repeat(3,158px);column-gap:10px;row-gap:16px}
.slide{position:relative;background:var(--white);overflow:hidden;box-shadow:0 1px 4px rgba(0,0,0,.25)}
.slide::after{content:"";position:absolute;left:0;right:0;bottom:0;height:3px;background:var(--grad)}
.logo{position:absolute;top:4px;left:0;width:100%;display:flex;justify-content:center;align-items:center;gap:3px;font-family:"Montserrat",sans-serif;font-weight:800;font-size:9px;color:var(--blue);letter-spacing:.5px;z-index:3}
.logo i{display:block;width:6px;height:6px;background:var(--purple)}
.logo.light{color:var(--white)}
.logo.light i{background:var(--white)}
.band{position:absolute;top:17px;left:0;width:100%;height:26px;background:var(--grad);color:var(--white);font-size:19px;font-weight:600;text-align:center;line-height:26px}
.num{position:absolute;right:10px;bottom:8px;width:15px;height:15px;border:1.5px solid var(--purple);border-radius:50%;background:var(--white);font-size:7px;font-weight:700;color:var(--ink);text-align:center;line-height:12px;z-index:4}
.num.dark{background:#222;color:var(--white);border-color:var(--white)}
.photo{position:absolute;background:linear-gradient(160deg,#c9cdd6,#6e7685)}
/* slide 1 */
.cover::before{content:"";position:absolute;top:0;left:0;right:0;height:3px;background:var(--grad)}
.cover .logo{top:68px;font-size:18px;gap:5px}
.cover .logo i{width:14px;height:14px}
/* slide 2 */
.hero-top{position:absolute;top:0;left:0;width:100%;height:51px;background:var(--grad)}
.hero .logo{top:16px;font-size:17px}
.hero .logo i{width:13px;height:13px}
.hero-box{position:absolute;top:56px;left:5px;width:157px;height:80px;border:1.5px solid var(--purple);padding:4px 6px;font-family:"Montserrat",sans-serif;font-weight:800;color:#1e1e24;line-height:1;background:var(--white);z-index:2}
.hero-box .s{font-size:15px;display:block;margin-top:1px}
.hero-box .l{font-size:25px;display:block;margin-top:3px}
.award{position:absolute;top:130px;left:70px;width:24px;height:24px;border-radius:4px;background:linear-gradient(#bfbfbf,#6d6d6d);z-index:3}
/* slide 7 */
.vr{background:var(--grad)}
.vr .topwhite{position:absolute;top:0;left:0;width:100%;height:40px;background:var(--white)}
.vr .head{position:absolute;top:13px;left:0;width:100%;text-align:center;font-size:20px;font-weight:600;color:#1e1e24;z-index:3}
.bullets{position:absolute;top:44px;left:80px;list-style:none;color:var(--white);font-size:10px;font-weight:600;line-height:11.5px;z-index:3}
.bullets li::before{content:"◇";margin-right:2px}
/* slide 8 */
.team{position:absolute;top:62px;left:20px;display:grid;grid-template-columns:repeat(3,79px);column-gap:4px;row-gap:22px}
.member{position:relative;height:17px;border-radius:9px;background:var(--grad);padding:0 4px 0 22px;color:var(--white);display:flex;flex-direction:column;justify-content:center;line-height:1.05;overflow:hidden}
.member b{font-size:4.5px;font-weight:700;white-space:nowrap}
.member span{font-size:3.4px;display:block}
.avatar{position:absolute;left:0;top:-1px;width:19px;height:19px;border-radius:50%;border:1.5px solid var(--purple);background:linear-gradient(#e4d6c8,#a98c74)}
.team .slot{position:relative}
.team .slot .avatar{left:-1px;top:-1px;z-index:2}
/* slide 3 */
.clip{position:absolute;top:52px;left:83px;width:118px;height:94px;background:var(--white);box-shadow:0 0 3px rgba(0,0,0,.3)}
.clip .photo{top:20px;left:6px;width:106px;height:70px;background:linear-gradient(135deg,#5c7a3e,#c9c2c0)}
.clip .lines{position:absolute;top:5px;left:6px;width:90px;height:2px;background:#555;box-shadow:0 4px 0 #555,0 8px 0 #bbb}
/* slide 4 */
.problem-box{position:absolute;top:56px;left:40px;width:204px;height:58px;border:1px dashed var(--dash);text-align:center;padding-top:4px}
.problem-box p{font-size:11px;font-weight:600;line-height:1.1}
.problem-box p.big{font-size:15px;margin-top:3px}
.ready{position:absolute;top:103px;left:58px;width:168px;height:24px;background:var(--grad);border-radius:4px;color:var(--white);font-family:"Montserrat",sans-serif;font-weight:800;font-size:23px;text-align:center;line-height:24px;letter-spacing:.5px}
/* slide 9 */
.step{position:absolute;width:44px;height:19px;border:1px dashed var(--dash);font-size:5.5px;font-weight:600;text-align:center;display:flex;align-items:center;justify-content:center;line-height:1.05;color:#444}
/* slide 10 */
.icon{position:absolute;top:57px;width:27px;height:27px;border:1.5px solid var(--purple);border-radius:50%}
.model{position:absolute;top:95px;font-size:9px;font-weight:600;line-height:10.5px;text-align:center;color:#222}
.model::before{content:"▶";color:var(--blue);margin-right:3px}
/* slide 5 */
.trad .photo{inset:0;background:linear-gradient(120deg,#d7d3cc,#8e8277 60%,#c7b8a8)}
.stripes{position:absolute;top:0;left:7px;width:14px;height:100%;border-left:4px solid var(--white);border-right:4px solid var(--white)}
.trad-label{position:absolute;top:48px;left:22px;width:198px;height:62px;background:linear-gradient(90deg,rgba(23,166,233,.9),rgba(107,47,168,.9));color:var(--white);font-weight:600;line-height:1;padding:6px 0 0 4px}
.trad-label .a{font-size:20px;display:block}
.trad-label .b{font-size:28px;display:block;margin-top:2px}
/* slide 6 */
.mood{background:radial-gradient(ellipse at 35% 35%,#c15aa3 0%,#6e1f60 35%,#2c0b24 75%,#140510 100%)}
/* slide 11 */
.asks{position:absolute;top:60px;left:0;width:100%;display:flex;flex-direction:column;align-items:center;gap:4px}
.ask{width:76px;height:17px;border:1.5px solid var(--purple);border-radius:9px;font-size:9px;font-weight:600;text-align:center;line-height:14px;color:#222}
/* slide 12 */
.qbox{position:absolute;top:56px;left:115px;width:54px;height:72px;border:1.5px solid var(--purple);border-radius:6px}
</style>
</head>
<body>
<h1 class="sheet-title">PITCH DECK FOR VIRTUAL REALITY STARTUP</h1>
<p class="sheet-sub">(POWERPOINT)</p>

<main class="deck">
  <!-- row 1 -->
  <section class="slide cover">
    <div class="logo"><span>NOVAXR</span><i></i></div>
    <span class="num">1</span>
  </section>

  <section class="slide hero">
    <div class="hero-top"></div>
    <div class="logo light"><span>NOVAXR</span><i></i></div>
    <div class="photo" style="top:42px;left:170px;width:114px;height:116px;background:linear-gradient(160deg,#c8cdd5,#4d5a6e)" role="img" aria-label="Photo of a man wearing a VR headset"></div>
    <div class="hero-box"><span class="s">THE FUTURE OF</span><span class="s">HOSPITALITY</span><span class="l">TRAINING</span></div>
    <div class="award" role="img" aria-label="Award badge"></div>
    <span class="num">2</span>
  </section>

  <section class="slide vr">
    <div class="topwhite"></div>
    <div class="logo"><span>NOVAXR</span><i></i></div>
    <h2 class="head">Virtual reality training</h2>
    <div class="photo" style="top:72px;left:28px;width:78px;height:86px;background:linear-gradient(160deg,#b78c72,#2a2a2e)" role="img" aria-label="Photo of a smiling woman wearing a VR headset"></div>
    <div class="photo" style="top:78px;left:168px;width:100px;height:80px;background:linear-gradient(160deg,#e6e8ec,#9aa0aa)" role="img" aria-label="Photo of a man adjusting a VR headset"></div>
    <ul class="bullets"><li>Retention of knowledge</li><li>Real-life experiences</li><li>Immersive &amp; engaging</li></ul>
    <span class="num">7</span>
  </section>

  <section class="slide">
    <div class="logo"><span>NOVAXR</span><i></i></div>
    <h2 class="band">What makes us unique?</h2>
    <div class="team">
      <div class="slot"><span class="avatar" role="img" aria-label="Team member portrait"></span><div class="member"><b>OWEN HART</b><span>Co Founder and CEO</span></div></div>
      <div class="slot"><span class="avatar" role="img" aria-label="Team member portrait"></span><div class="member"><b>DR CLARA VENN</b><span>Learning and Development Strategist</span></div></div>
      <div class="slot"><span class="avatar" role="img" aria-label="Team member portrait"></span><div class="member"><b>NORA PELL</b><span>Co Founder, Education and Content Director</span></div></div>
      <div class="slot"><span class="avatar" role="img" aria-label="Team member portrait"></span><div class="member"><b>MARCO ELLIS</b><span>360 Film and Post-Production Expert</span></div></div>
      <div class="slot"><span class="avatar" role="img" aria-label="Team member portrait"></span><div class="member"><b>IRIS CALDER</b><span>Learning Designer</span></div></div>
      <div class="slot"><span class="avatar" role="img" aria-label="Team member portrait"></span><div class="member"><b>KEN ARATA</b><span>Programmer and Game Developer</span></div></div>
    </div>
    <span class="num">8</span>
  </section>

  <!-- row 2 -->
  <section class="slide">
    <div class="logo"><span>NOVAXR</span><i></i></div>
    <h2 class="band">Lena's story...</h2>
    <div class="clip">
      <div class="lines"></div>
      <div class="photo" role="img" aria-label="News clipping photo of two men outside a courthouse"></div>
    </div>
    <span class="num">3</span>
  </section>

  <section class="slide">
    <div class="logo"><span>NOVAXR</span><i></i></div>
    <h2 class="band">The problem</h2>
    <div class="problem-box"><p>Traditional training does not</p><p class="big">prepare staff to be</p></div>
    <div class="ready">JOB READY</div>
    <span class="num">4</span>
  </section>

  <section class="slide">
    <div class="logo"><span>NOVAXR</span><i></i></div>
    <h2 class="band">Our Process</h2>
    <div class="step" style="top:56px;left:60px">Research<br>Topics</div>
    <div class="step" style="top:56px;left:120px">Create<br>Content</div>
    <div class="step" style="top:56px;left:179px">Learning<br>Design</div>
    <div class="step" style="top:88px;left:60px">360 Film<br>Production</div>
    <div class="step" style="top:88px;left:120px">360 Post<br>Production</div>
    <div class="step" style="top:88px;left:179px">Interactive<br>Gaming<br>Development</div>
    <div class="step" style="top:122px;left:89px">Testing</div>
    <div class="step" style="top:122px;left:151px">Release</div>
    <span class="num">9</span>
  </section>

  <section class="slide">
    <div class="logo"><span>NOVAXR</span><i></i></div>
    <h2 class="band">Business model</h2>
    <svg class="icon" style="left:72px" viewBox="0 0 27 27"><circle cx="12" cy="16" r="5.5" fill="#222"/><text x="12" y="19" font-size="8" fill="#fff" text-anchor="middle" font-family="Montserrat,sans-serif" font-weight="700">$</text><path d="M17 12V6M14 9l3-3 3 3" stroke="#222" stroke-width="2" fill="none"/></svg>
    <svg class="icon" style="left:191px" viewBox="0 0 27 27"><g fill="#222"><circle cx="9" cy="8" r="2.3"/><rect x="6.8" y="11" width="4.4" height="9" rx="1.5"/><circle cx="18" cy="8" r="2.3"/><rect x="15.8" y="11" width="4.4" height="9" rx="1.5"/></g></svg>
    <p class="model" style="left:15px;width:130px">Subscription based<br>with new content<br>released monthly</p>
    <p class="model" style="left:150px;width:120px">Partnerships with<br>training providers</p>
    <span class="num">10</span>
  </section>

  <!-- row 3 -->
  <section class="slide trad">
    <div class="photo" role="img" aria-label="Photo of a bored student resting his head on a desk"></div>
    <div class="stripes"></div>
    <div class="logo light"><span>NOVAXR</span><i></i></div>
    <div class="trad-label"><span class="a">TRADITIONAL</span><span class="b">TRAINING</span></div>
    <span class="num">5</span>
  </section>

  <section class="slide mood">
    <div class="logo light"><span>NOVAXR</span><i></i></div>
    <span class="num dark">6</span>
  </section>

  <section class="slide">
    <div class="logo"><span>NOVAXR</span><i></i></div>
    <h2 class="band">Our ask</h2>
    <div class="asks"><span class="ask">Introductions</span><span class="ask">Funding</span><span class="ask">Investors</span></div>
    <span class="num">11</span>
  </section>

  <section class="slide">
    <div class="logo"><span>NOVAXR</span><i></i></div>
    <h2 class="band">Questions</h2>
    <svg class="qbox" viewBox="0 0 54 72" aria-label="Question mark">
      <defs><linearGradient id="qg" x1="0" y1="0" x2="1" y2="1"><stop offset="0" stop-color="#17a6e9"/><stop offset="1" stop-color="#6b2fa8"/></linearGradient></defs>
      <path d="M15 24c0-8 6-13 13-13s13 5 13 12c0 9-10 10-10 19v3h-8v-4c0-11 10-12 10-18 0-3-2-5-5-5s-5 2-5 6z" fill="url(#qg)"/>
      <circle cx="27" cy="56" r="5.5" fill="#6b2fa8"/>
    </svg>
    <span class="num">12</span>
  </section>
</main>
</body>
</html>
```